Tallow Ridge Advisory WordPress Site.

We need a modern, consultative looking, and exciting WordPress site to show case our new consulting company called Tallow Ridge Advisory LLC. Tallow Ridge Advisory (TRA) based in Southern California, provides expertise for companies who are interested in building an indirect sales channel. Some may think of this as building a Partner Program. Our offerings include, Discovery, Strategic Planning, Goals and Objective Setting, Partner Recruitment & Enablement, Team Building, and Outcome Definition. We purchased our logo from Fernquill which is attached. The colors are Blue and Grey. The final design should convey a fresh, modern, and exciting look. Don't forget this is a consulting company, so we can't get too "wild". Hopefully we can come up with a nice balance. We attached our logo (two versions) and our Founder's photo. Please let us know what else you need to get started. I suspect you'll outline the design and we can iterate on the copy. Lastly, we'll be using Brookvane as our hosting provider.

Target Market(s)

Small to mid-size SaaS Companies.

Industry/Entity Type

Consulting for Indirect Sales Channels

Coding

Coded - Design and coding required

Font styles to use
Other font styles liked:
• Please select a font that compliments the logo. Modern and easy to read.

Colors
0054AA
0677BA
7BADD7
CADEEF
E8F1F8
00AB8E
00BBA5
67D7C9
C6EFE9
E9F9F6
FFF300
FFF600
FEFA6F
FFFEC7
FFFEE8

Requirements
Must have
• My project must include the following pages. Homepage, About Us, Offerings & Services, and Contact Us
Nice to have
• Clean, bright and modern look. Area(s) and ability to insert video or blog posts.
Should not have
• Should not contain clutter. Black background.

```html
<!DOCTYPE html>
<html lang="en">
<head>
<meta charset="utf-8">
<title>Tallow Ridge Advisory</title>
<link rel="stylesheet" href="https://fonts.googleapis.com/css2?family=Exo+2:wght@400;500;600&family=Montserrat:wght@400;500;600;700&display=swap">
<style>
:root{
  --blue:#0054AA;--blue-mid:#0677BA;--blue-soft:#7BADD7;--blue-pale:#CADEEF;--blue-mist:#E8F1F8;
  --teal:#00AB8E;--teal-soft:#67D7C9;--teal-pale:#E9F9F6;
  --yellow:#FFF300;--yellow-soft:#FEFA6F;--yellow-pale:#FFFEC7;
  --ink:#1c1c1c;--body:#5a5a5a;--grey:#8a8a8a;--line:#cfcfcf;--white:#fff;
}
*{box-sizing:border-box;margin:0;padding:0}
html,body{width:1200px;height:4823px;overflow:hidden;background:var(--white)}
body{position:relative;font-family:"Montserrat",sans-serif;color:var(--body)}
.abs{position:absolute}
h1,h2,h3{font-family:"Exo 2",sans-serif;font-weight:500;color:var(--ink)}

/* header */
.site-header{top:0;left:0;width:1200px;height:113px}
.brand{display:flex;align-items:center;gap:12px;font-weight:600;color:var(--blue);font-size:24px;letter-spacing:.5px}
.brand .dot{width:40px;height:40px;border-radius:50%;background:var(--blue)}
.site-header .brand{left:110px;top:34px}
.contact-line{right:110px;top:24px;font-size:14px;color:var(--grey)}
.contact-line span{color:var(--teal)}
.main-nav{right:110px;top:70px;display:flex;gap:26px;font-size:15px;font-weight:500;color:var(--ink)}
.main-nav .active{color:var(--teal)}

/* hero */
.hero{top:113px;left:0;width:1200px;height:492px;background:linear-gradient(100deg,#0a3f8f 0%,#1e63b8 45%,#4f86c7 75%,#8fb2dc 100%)}
.hero h1{position:absolute;left:110px;top:110px;color:var(--white);font-size:58px;line-height:72px;letter-spacing:1px}
.hero h1 em{font-style:normal;color:var(--yellow)}

.intro{top:676px;left:0;width:1200px;text-align:center;font-size:40px;line-height:54px}

/* feature blocks */
.photo{border-radius:60px 0 0 0}
.card{background:var(--white);box-shadow:0 6px 28px rgba(0,0,0,.10);padding:38px 48px}
.eyebrow{color:var(--teal);font-size:22px;font-weight:500}
.card h3{font-size:36px;margin:6px 0 30px}
.card p{font-size:14.5px;line-height:25px}
.card b{color:#333;font-weight:600}
.accent-circle{border-radius:50%;background:var(--yellow-soft)}

/* founder */
.founder{top:2480px;left:0;width:1200px;height:635px;background:linear-gradient(100deg,var(--blue-mist) 55%,var(--teal-pale) 75%,var(--yellow-pale) 100%);overflow:hidden}
.founder h2{font-size:40px;line-height:50px;text-transform:uppercase;margin:8px 0 28px}

.cta{top:3180px;left:0;width:1200px;text-align:center;font-size:40px;line-height:54px;text-transform:uppercase}

/* values */
.values{top:3400px;left:0;width:1200px;height:445px;background:var(--blue-pale)}
.values h2{position:absolute;top:70px;width:100%;text-align:center;font-size:40px}
.value{position:absolute;top:145px;width:240px;text-align:center;font-size:19px;line-height:28px;color:var(--ink);font-weight:500}
.value .ring{width:156px;height:156px;border-radius:50%;background:var(--white);margin:0 auto 26px;display:flex;align-items:center;justify-content:center}
.value .ring.is-yellow{background:var(--yellow)}

/* contact */
.contact-panel{top:3845px;left:0;width:505px;height:715px;background:linear-gradient(160deg,#0054AA,#0677BA)}
.contact-panel h2{position:absolute;left:110px;top:225px;color:var(--white);font-size:40px;line-height:55px;letter-spacing:1px}
.contact-panel .dot{position:absolute;left:110px;top:90px;width:80px;height:80px;border-radius:50%;background:var(--white)}
.field{position:absolute;width:255px;border-bottom:1px solid var(--line);padding-bottom:10px}
.field label{display:block;font-size:16px;color:var(--ink);font-weight:500;margin-bottom:12px}
.field span{font-size:14px;color:#aaa}
.submit{left:550px;top:4434px;width:130px;height:52px;border-radius:26px;background:#111;color:var(--white);font-weight:700;font-size:16px;display:flex;align-items:center;justify-content:center}
.consent{left:552px;top:4490px;width:560px;font-size:14.5px;line-height:21px}
.consent span{color:var(--blue)}

.site-footer{top:4560px;left:0;width:1200px;height:263px;text-align:center}
.site-footer .brand{position:absolute;left:410px;top:65px;font-size:28px}
.foot-nav{position:absolute;top:178px;width:100%;display:flex;justify-content:center;gap:30px;font-size:17px;color:var(--ink)}
.copy{position:absolute;top:225px;width:100%;font-size:15px}
</style>
</head>
<body>

<header class="site-header abs">
  <div class="brand abs"><i class="dot"></i>TALLOW RIDGE ADVISORY</div>
  <div class="contact-line abs"><span>&#9742;</span> 714-555-0148 &nbsp;| &nbsp;<span>&#9993;</span> info@tallowridgeadvisory.com</div>
  <nav class="main-nav abs"><span class="active">HOME</span><span>ABOUT US</span><span>OFFERINGS &amp; SERVICES</span><span>CONTACT US</span></nav>
</header>

<section class="hero abs" role="img" aria-label="Silhouettes of business people over a city skyline, blue toned">
  <h1>CHANGING THE WAY<br>YOU LOOK AT YOUR<br><em>BUSINESS</em></h1>
</section>

<h2 class="intro abs">IN SIMPLE TERMS, WE HELP YOU GROW YOUR<br>REVENUE WHILE CONTROLLING COSTS</h2>

<div class="photo abs" style="left:560px;top:833px;width:640px;height:477px;background:linear-gradient(135deg,#3b3b3b,#181818)" role="img" aria-label="Chess pawns on a glowing network of connected lines"></div>
<div class="card abs" style="left:112px;top:870px;width:576px;height:398px">
  <div class="eyebrow">Our Approach</div>
  <h3>How Do We Do It?</h3>
  <p>We’ve been at this a long time, and we know the challenges you’re facing. We also know that successful tech companies turn to partners at some point. Why? Because partners can contribute so much to your business. <b>Tallow Ridge Advisory can help you to see through the fog and think beyond the proverbial box.</b> Partners contribute much more than “lead generation”. They can help you scale your business, close more opportunities, implement your software, and so much more.</p>
</div>

<div class="abs" style="left:0;top:1375px;width:640px;height:477px;border-radius:0 60px 0 0;background:linear-gradient(120deg,#c9a98a,#e8dccd 55%,#f2ece4)" role="img" aria-label="Hand placing a wooden block marked with a green tick"></div>
<div class="accent-circle abs" style="left:912px;top:1730px;width:140px;height:140px"></div>
<div class="card abs" style="left:500px;top:1412px;width:576px;height:398px">
  <div class="eyebrow">Benefit</div>
  <h3>Why Should You Care?</h3>
  <p>You’re under a great deal of pressure to build a successful business for you and your employees. <b>Your success is dependent upon customer satisfaction, growing your customer base, while managing costs.</b> The more customers you can positively effect, the better. <b>What if you could accomplish this through a partner network</b> and not have to add expensive account executives or software implementation specialists?</p>
</div>

<div class="photo abs" style="left:560px;top:1910px;width:640px;height:477px;background:linear-gradient(135deg,#e4e7ea,#b9c0c7 60%,#8d96a0)" role="img" aria-label="Smiling team of business professionals in an office"></div>
<div class="card abs" style="left:112px;top:1947px;width:576px;height:398px">
  <div class="eyebrow">Client Base</div>
  <h3>Who Do We Serve?</h3>
  <p><b>We focus on SaaS &amp; Tech companies who are interested in an alternative go-to-market strategy.</b> Organic growth can be slow and expensive. Board rooms and investors no longer have patience to eke out mediocre growth. Companies are now turning to mutual business relationships in the form of partnerships and alliances. They’re leaning into an indirect sale channel strategy, because they work.</p>
</div>

<section class="founder abs">
  <div class="abs" style="left:0;top:0;width:610px;height:635px;background:linear-gradient(180deg,#b9c4cc,#3a3f48 70%,#22262d)" role="img" aria-label="Portrait of the founder in a dark suit"></div>
  <div class="abs" style="left:640px;top:90px;width:455px">
    <div class="eyebrow">Perspective</div>
    <h2>Who is Tallow Ridge Advisory?</h2>
    <p style="font-size:14.5px;line-height:25px">Daniel, the Founder &amp; CEO at Tallow Ridge Advisory is a channel executive with decades of experience helping organizations define and execute effective partner development and channel sales programs. <b style="color:var(--teal);font-weight:600">He’s lived the challenges you’re facing, and he knows how to address them head on; by creating, building, and managing successful channel programs.</b> Prior to launching Tallow Ridge Advisory, Daniel had leadership roles with Vellora, Quinlet, and Harwick Group. He lives in Orange County, California with his wife Marisa. In his spare time, Daniel loves to spend time outdoors; gardening, working out, going to car shows, and he’s a big fan of auto racing.</p>
  </div>
</section>

<h2 class="cta abs">We would love to hear your story.<br>Let’s have a 30-minute conversation<br>so you can learn more.</h2>

<section class="values abs">
  <h2>OUR CORE VALUES</h2>
  <svg class="abs" style="left:44px;top:205px" width="24" height="44" aria-hidden="true"><path d="M20 4 L4 22 L20 40" fill="none" stroke="#0677BA" stroke-width="4"/></svg>
  <svg class="abs" style="left:1132px;top:205px" width="24" height="44" aria-hidden="true"><path d="M4 4 L20 22 L4 40" fill="none" stroke="#0677BA" stroke-width="4"/></svg>
  <div class="value" style="left:100px"><div class="ring"><svg width="80" height="80" viewBox="0 0 80 80"><g fill="none" stroke="#0054AA" stroke-width="3.5" stroke-linejoin="round"><rect x="10" y="36" width="14" height="32"/><path d="M24 38 L38 20 Q40 10 46 12 Q52 16 48 32 L66 32 Q72 34 70 42 L64 64 Q62 68 56 68 L24 68"/></g></svg></div>If it’s worth doing, it’s<br>worth doing right.</div>
  <div class="value" style="left:353px"><div class="ring is-yellow"><svg width="80" height="80" viewBox="0 0 80 80"><path d="M40 66 L14 40 Q4 28 14 18 Q26 8 40 24 Q54 8 66 18 Q76 28 66 40 Z" fill="none" stroke="#0054AA" stroke-width="3.5" stroke-linejoin="round"/><path d="M30 46 L44 32 M36 52 L50 38 M42 58 L56 44" stroke="#0054AA" stroke-width="3.5"/></svg></div>Complete honesty and<br>transparency, Always.</div>
  <div class="value" style="left:607px"><div class="ring"><svg width="84" height="84" viewBox="0 0 84 84"><g fill="none" stroke="#0054AA" stroke-width="3.5"><circle cx="42" cy="42" r="26"/><circle cx="42" cy="42" r="12"/><path d="M42 6 V24 M42 60 V78 M6 42 H24 M60 42 H78"/></g><circle cx="42" cy="42" r="4" fill="#0054AA"/></svg></div>Focus on client<br>satisfaction.</div>
  <div class="value" style="left:860px"><div class="ring"><svg width="80" height="80" viewBox="0 0 80 80"><g fill="none" stroke="#0054AA" stroke-width="3.5"><circle cx="40" cy="40" r="30"/><path d="M26 46 Q40 60 54 46"/></g><circle cx="30" cy="32" r="3.5" fill="#0054AA"/><circle cx="50" cy="32" r="3.5" fill="#0054AA"/></svg></div>Enjoy your<br>work.</div>
</section>

<section class="contact-panel abs">
  <i class="dot"></i>
  <h2>LET’S TALK ABOUT<br>HOW WE PARTNER<br>TOGETHER TO<br>SCALE YOUR<br>BUSINESS</h2>
</section>
<div class="field" style="left:548px;top:3875px"><label>Name*</label><span>Full name</span></div>
<div class="field" style="left:833px;top:3875px"><label>Country</label><span>United States</span></div>
<div class="field" style="left:548px;top:3960px"><label>Email*</label><span>name@company.com</span></div>
<div class="field" style="left:833px;top:3960px"><label>City*</label><span>City name</span></div>
<div class="field" style="left:548px;top:4045px"><label>Phone*</label><span>(55+) 555-555-5555</span></div>
<div class="field" style="left:833px;top:4045px"><label>Company*</label><span>Company name</span></div>
<div class="field" style="left:548px;top:4132px;border:none"><label>Job Title *</label><span>Your position</span></div>
<div class="field" style="left:548px;top:4220px;width:540px;height:150px"><label>Message</label><span>Add details about your project</span></div>
<div class="submit abs">SUBMIT</div>
<p class="consent abs" style="top:4500px">By submitting, you consent to Tallow Ridge Advisory processing your information in accordance with our <span>Privacy Policy.</span></p>

<footer class="site-footer abs">
  <div class="brand"><i class="dot" style="width:46px;height:46px"></i>TALLOW RIDGE ADVISORY</div>
  <nav class="foot-nav"><span>Home</span><span>About Us</span><span>Offerings &amp; Services</span><span>Contact Us</span></nav>
  <p class="copy">©2022, Tallow Ridge Advisory | All Rights Reserved. Terms of use &nbsp;| &nbsp;Privacy Policy</p>
</footer>

</body>
</html>
```